Lowell Brandt

20 Year Licensed Master Barber specializing in:
men/women cuts, Grooming, Straight razor Shaving and tape line enhancement, beard grooming, eye brow enhancement, South of France, Hot Towel Treatments, Scalp, Blow outs, Shags, Custom Design,RazorCuts,Shear Cuts, Bobs, Perms, Relaxers, Shoe Shine.
Please create a wonderful business card incorporating all the info above and selecting one of the photos. Please be creative.

Barber

```html
<!DOCTYPE html>
<html lang="en">
<head>
<meta charset="utf-8">
<title>Lowell Brandt – Master Barber Business Card</title>
<link rel="stylesheet" href="https://fonts.googleapis.com/css2?family=Open+Sans:wght@400;700&display=swap">
<style>
  :root {
    --page-bg: #d9d8d6;
    --card-bg: #141517;
    --card-edge: #1f2023;
    --text-light: #d7d8dc;
    --text-muted: #a9abb1;
    --accent-blue: #4d55b8;
    --badge-white: #f1f1f3;
    --photo-warm: #b88a6c;
    --photo-deep: #5a3a2c;
  }
  * { box-sizing: border-box; margin: 0; padding: 0; }
  html, body {
    width: 1200px; height: 864px; overflow: hidden;
    background: var(--page-bg);
    font-family: "Open Sans", Arial, sans-serif;
  }
  .card-set {
    position: absolute; inset: 0;
    display: flex; align-items: center; justify-content: center; gap: 36px;
  }
  .card {
    position: relative; width: 560px; height: 320px;
    background: linear-gradient(160deg, var(--card-edge), var(--card-bg));
    overflow: hidden;
    box-shadow: 0 6px 18px rgba(0,0,0,.25);
  }
  .brand-mark {
    display: flex; align-items: center; gap: 10px;
  }
  .brand-mark__dot {
    width: 22px; height: 22px; border-radius: 50%;
    background: var(--badge-white);
  }
  .brand-mark__name {
    font-weight: 700; font-size: 22px; letter-spacing: 1px;
    color: var(--text-light); text-transform: uppercase;
  }
  /* Back face */
  .card--back { display: flex; flex-direction: column; align-items: center; padding: 46px 40px 0; }
  .card--back .brand-mark { margin-bottom: 34px; }
  .services__title {
    font-weight: 700; font-size: 15px; color: var(--text-light);
    text-align: center; margin-bottom: 6px;
  }
  .services__list {
    font-size: 13.5px; line-height: 1.5; color: var(--text-muted);
    text-align: center;
  }
  /* Front face */
  .card--front .brand-mark { position: absolute; left: 44px; top: 62px; }
  .contact-list {
    position: absolute; left: 44px; top: 168px; list-style: none;
    font-size: 14px; color: var(--text-light);
  }
  .contact-list li { display: flex; align-items: center; gap: 10px; height: 24px; }
  .contact-list svg { width: 14px; height: 14px; flex: none; }
  .portrait {
    position: absolute; right: 0; bottom: 0; width: 210px; height: 250px;
    background: radial-gradient(ellipse at 50% 35%, var(--photo-warm), var(--photo-deep) 75%, var(--card-bg));
  }
</style>
</head>
<body>
  <main class="card-set">
    <section class="card card--back">
      <div class="brand-mark">
        <span class="brand-mark__dot"></span>
        <span class="brand-mark__name">Lowell Brandt</span>
      </div>
      <p class="services__title">20 Year Licensed Master Barber specializing in</p>
      <p class="services__list">
        men/women cuts, Grooming Straight razor Shaving and tape line<br>
        enhancement beard grooming, eye brow enhancement,<br>
        South of France Hot Towel Treatments, Scalp, Blow outs, Shags,<br>
        Custom Design RazorCuts,Shear Cuts, Bobs<br>
        Perms, Relaxers, Shoe Shine.
      </p>
    </section>

    <section class="card card--front">
      <div class="brand-mark">
        <span class="brand-mark__dot"></span>
        <span class="brand-mark__name">Lowell Brandt</span>
      </div>
      <ul class="contact-list">
        <li>
          <svg viewBox="0 0 14 14" aria-hidden="true"><path fill="var(--accent-blue)" d="M3 1h2.5l1 3-1.6 1.2a8 8 0 0 0 3.9 3.9L10 7.5l3 1V11a2 2 0 0 1-2 2A10 10 0 0 1 1 3a2 2 0 0 1 2-2z"/></svg>
          (555)318-4406
        </li>
        <li>
          <svg viewBox="0 0 14 14" aria-hidden="true"><rect x="1" y="3" width="12" height="8" fill="var(--accent-blue)"/><path d="M1 3l6 5 6-5" fill="none" stroke="var(--card-bg)" stroke-width="1.2"/></svg>
          lowell.brandt3@mailbox.com
        </li>
        <li>
          <svg viewBox="0 0 14 14" aria-hidden="true"><rect x="1" y="1" width="12" height="12" rx="2" fill="var(--accent-blue)"/></svg>
          3lbrandt
        </li>
        <li>
          <svg viewBox="0 0 14 14" aria-hidden="true"><rect x="1" y="1" width="12" height="12" rx="2" fill="var(--accent-blue)"/></svg>
          Lowell.brandt3
        </li>
      </ul>
      <div class="portrait" role="img" aria-label="Portrait photo of the barber in a tweed flat cap and glasses, hand at chin"></div>
    </section>
  </main>
</body>
</html>
```